Stretch on the Green with Mara

I want to advertise my Stretch on the Green classes for Summer. Classes are outside at the lovely local park. Dunmore field. 82 Halcombe St. Westlow.
Classes are for beginners to advance levels.
Classes start Monday, October 17th.
Monday 6pm Beginners
Tuesday 6pm Intermediate
Thursday 6pm Intermediate/Advance
Saturday 9am All fitness levels
My Pilates classes are specially designed to help improve strength and flexibility but as well will also improve posture, reduce stress and develop control and endurance in the entire body.
Booking essential. Limited numbers so I can make sure the correct technique is always being followed.
For more info or to book contact details:
Mara 027385916
mara@corestudiomara.net
www.corestudiomara.net
$15 Per Session

Target Market(s)

Males and Females ages 35plus.

Industry/Entity Type

Fitness

Font styles to use
Sans Serif

Requirements
Must have
• My logo. Contact details. A Park that looks lovely to exercise at.
Nice to have
• Summer looking. Trees - inspiration to be exercising outside

```html
<!DOCTYPE html>
<html lang="en">
<head>
<meta charset="utf-8">
<title>Stretch on the Green with Mara</title>
<link href="https://fonts.googleapis.com/css2?family=Lato:ital,wght@0,300;0,400;0,700;1,400&display=swap" rel="stylesheet">
<style>
  :root {
    --pink: #f087b5;
    --pink-deep: #d0729f;
    --pink-text: #c8629a;
    --pink-wash: #fbe3ee;
    --ink: #4a4a4a;
    --grey-text: #6a6a6a;
    --footer-dark: #4b4b4b;
    --footer-light: #8e8e8e;
    --white: #ffffff;
  }
  * { margin: 0; padding: 0; box-sizing: border-box; }
  html, body { width: 927px; height: 1200px; overflow: hidden; background: var(--white); }
  body { font-family: 'Lato', sans-serif; }
  .flyer { position: relative; width: 927px; height: 1200px; overflow: hidden; background: var(--white); }

  .park-scene {
    position: absolute; left: 0; top: 0; width: 927px; height: 580px;
    background:
      radial-gradient(ellipse 160px 120px at 600px 20px, rgba(255,250,220,.95), rgba(255,250,220,0) 70%),
      radial-gradient(ellipse 420px 160px at 420px 420px, rgba(240,235,150,.85), rgba(240,235,150,0) 70%),
      radial-gradient(ellipse 300px 260px at 80px 180px, #2f5a1e, rgba(47,90,30,0) 75%),
      radial-gradient(ellipse 300px 260px at 860px 160px, #3b6a22, rgba(59,106,34,0) 75%),
      linear-gradient(180deg, #4f7a2c 0%, #8aa844 35%, #c9cf6a 62%, #e8dfa0 78%, #f6e9ea 92%, rgba(255,255,255,0) 100%);
  }
  .photo-fade {
    position: absolute; left: 0; top: 470px; width: 927px; height: 120px;
    background: linear-gradient(180deg, rgba(255,255,255,0), #ffffff 85%);
  }
  .pink-wash {
    position: absolute; left: 0; top: 560px; width: 927px; height: 400px;
    background:
      radial-gradient(ellipse 380px 170px at 150px 210px, rgba(246,190,215,.7), rgba(246,190,215,0) 75%),
      radial-gradient(ellipse 420px 130px at 700px 250px, rgba(248,205,222,.65), rgba(248,205,222,0) 75%),
      radial-gradient(ellipse 500px 110px at 460px 340px, rgba(250,215,230,.5), rgba(250,215,230,0) 75%);
  }

  .title { position: absolute; left: 0; top: 70px; width: 927px; text-align: center; color: var(--white); font-weight: 300; }
  .title-main { display: block; font-size: 128px; line-height: 1; letter-spacing: 10px; }
  .title-sub { display: block; font-size: 84px; line-height: 1; letter-spacing: 6px; margin-top: 16px; }
  .title-with { display: block; font-size: 30px; letter-spacing: 22px; margin-top: 8px; font-weight: 400; }

  .price-card {
    position: absolute; left: 55px; top: 447px; width: 338px; height: 119px;
    background: var(--pink); border-radius: 10px; overflow: hidden; color: var(--white); text-align: center;
  }
  .price-card-intro { font-size: 24px; line-height: 28px; padding-top: 14px; font-weight: 400; }
  .price-card-price { position: absolute; left: 0; bottom: 10px; width: 100%; height: 30px; line-height: 30px; background: var(--pink-deep); font-size: 24px; }

  .start-date { position: absolute; left: 55px; top: 583px; font-size: 18px; color: var(--ink); }
  .schedule { position: absolute; left: 55px; top: 622px; }
  .schedule-row { display: flex; height: 39.5px; align-items: center; font-size: 25px; }
  .schedule-day { width: 113px; color: var(--ink); }
  .schedule-time { width: 62px; color: var(--ink); }
  .schedule-level { color: var(--pink-text); font-weight: 700; text-transform: uppercase; }

  .venue { position: absolute; left: 55px; top: 787px; display: flex; align-items: center; gap: 10px; font-style: italic; font-size: 21px; color: var(--ink); }
  .venue svg { width: 24px; height: 26px; }

  .about { position: absolute; left: 120px; top: 846px; width: 687px; text-align: center; font-size: 20px; line-height: 28.5px; font-weight: 300; color: var(--grey-text); }

  .footer { position: absolute; left: 0; top: 967px; width: 927px; height: 233px; background: var(--footer-dark); }
  .footer-strip { position: absolute; left: 0; top: 180px; width: 927px; height: 53px; background: var(--footer-light); }
  .footer-url { position: absolute; left: 64px; top: 180px; height: 53px; line-height: 53px; font-size: 25px; color: var(--white); }
  .brand-name { position: absolute; left: 40px; top: 130px; width: 335px; text-align: center; font-size: 28px; letter-spacing: 2px; color: var(--pink); font-weight: 400; }
  .brand-mark { position: absolute; left: 183px; top: 55px; width: 48px; height: 48px; border-radius: 50%; background: var(--footer-light); }

  .booking-note { position: absolute; left: 455px; top: 22px; width: 420px; text-align: center; font-size: 14.5px; line-height: 20px; font-weight: 300; color: #a3a3a3; }
  .contact-card { position: absolute; left: 454px; top: 64px; width: 420px; height: 169px; background: var(--pink); border-radius: 10px 10px 0 0; overflow: hidden; color: var(--white); }
  .contact-card-head { height: 49px; line-height: 49px; background: var(--pink-deep); text-align: center; font-size: 22px; font-weight: 300; }
  .contact-list { list-style: none; padding: 8px 0 0 47px; }
  .contact-item { display: flex; align-items: center; gap: 14px; height: 32px; font-size: 25px; }
  .contact-item svg { width: 22px; height: 22px; flex: none; }
</style>
</head>
<body>
<main class="flyer">
  <div class="park-scene" role="img" aria-label="Sunlit summer park with tall green trees and a woman stretching on a blue exercise mat"></div>
  <div class="photo-fade"></div>
  <div class="pink-wash"></div>

  <h1 class="title">
    <span class="title-main">STRETCH</span>
    <span class="title-sub">ON THE GREEN</span>
    <span class="title-with">WITH MARA</span>
  </h1>

  <div class="price-card">
    <p class="price-card-intro">Come and Join a<br>Stretch Session on the Green.</p>
    <p class="price-card-price">$15 Per Session</p>
  </div>

  <p class="start-date">Classes starts on Monday, October 17th.</p>
  <div class="schedule">
    <div class="schedule-row"><span class="schedule-day">Monday</span><span class="schedule-time">6pm</span><span class="schedule-level">Beginners</span></div>
    <div class="schedule-row"><span class="schedule-day">Tuesday</span><span class="schedule-time">6pm</span><span class="schedule-level">Intermediate</span></div>
    <div class="schedule-row"><span class="schedule-day">Thursday</span><span class="schedule-time">6pm</span><span class="schedule-level">Intermediate / Advance</span></div>
    <div class="schedule-row"><span class="schedule-day">Saturday</span><span class="schedule-time">9am</span><span class="schedule-level">All Fitness Levels</span></div>
  </div>

  <p class="venue">
    <svg viewBox="0 0 24 26" fill="none" stroke="#f087b5" stroke-width="1.6"><path d="M12 22s-7-7-7-12a7 7 0 0 1 14 0c0 5-7 12-7 12z"/><circle cx="12" cy="10" r="2.6"/><ellipse cx="12" cy="23" rx="8" ry="2"/></svg>
    Dunmore Field, 82 Halcombe St., Westlow, Harbourview 2086
  </p>

  <p class="about">My Pilates classes are specially designed to help improve strength and flexibility but as well will also improve posture, reduce stress and develop control and endurance in the entire body.</p>

  <footer class="footer">
    <div class="brand-mark"></div>
    <p class="brand-name">CORE STUDIO MARA</p>
    <div class="footer-strip"></div>
    <p class="footer-url">www.corestudiomara.net</p>

    <p class="booking-note">Booking essential. Limited numbers so I can make sure the correct technique is always being followed.</p>
    <div class="contact-card">
      <p class="contact-card-head">For more info or to book contact:</p>
      <ul class="contact-list">
        <li class="contact-item">
          <svg viewBox="0 0 22 22" fill="none" stroke="#fff" stroke-width="1.6"><circle cx="11" cy="7" r="4.5"/><path d="M3 21c0-5 3.5-8 8-8s8 3 8 8"/></svg>
          Mara
        </li>
        <li class="contact-item">
          <svg viewBox="0 0 22 22" fill="none" stroke="#fff" stroke-width="1.6"><path d="M5 3l3 4-2 2c1 3 4 6 7 7l2-2 4 3-2 3C9 20 2 13 2 5z"/><path d="M13 3a6 6 0 0 1 6 6M13 6a3 3 0 0 1 3 3"/></svg>
          027385916
        </li>
        <li class="contact-item">
          <svg viewBox="0 0 22 22" fill="none" stroke="#fff" stroke-width="1.6"><rect x="2" y="5" width="18" height="13"/><path d="M2 5l9 7 9-7"/></svg>
          mara@corestudiomara.net
        </li>
      </ul>
    </div>
  </footer>
</main>
</body>
</html>
```